依頼詳細
デザインを依頼する製品の名前は「雪嶺そば」です。
表面のデザイン作成をお願いします。

【デザインイメージ】
・シックで高級感のあるデザインが好ましいです。
・希望の色はベースが黒色で商品名の「雪嶺そば」は金色でお願いします。

【必須記載事項】
下記の文言は必ずデザイン上に記載をお願いします。
・ゆで時間4~5分
・内容量220g
・「謹製」(四角の判子風)
・「本場信州の伝統の味」
・「そばの豊かな香りと喉ごしの良さを楽しめます」

【その他製品特徴】
下記はその他製品の特徴になります。デザインへの記載は各ランサー様へお任せします。
・本品「雪嶺そば」は、本場信州の恵まれた気候風土と長年の経験の中から独自の製法を編み出し、生まれました。のどごしの良いなめらかな食感と風味豊かな香りを楽しめるそばに仕上げました。
・本品は贈答品で使用することが多いため、化粧箱に入っている状態で見栄えが良く見えるデザインをお願いします。また参考となる画像を添付いたします。
記載項目
製品サイズ(実寸):295×75(mm)
希望イメージ
シンプル 複雑
単色 カラフル
暗い 明るい
日常 高級
遊び心 厳粛
未来的 伝統的
女性的 男性的
希望する色
無彩色系
納品ファイル
• 高解像度JPG (.jpg)
• イラストレーター形式 (.ai)
補足説明
■ 選んだ理由

当社がイメージした通り、シックで高級感があり化粧箱に入っている状態で見栄えが良く見えるデザインで、社内のアンケートでも好評だったため選定させていただきました。

■ 提案者全員のお礼・コメント

この度は、たくさんのご提案を頂き、大変ありがとうございます。
さまざまなデザイン案やコンセプトがあり、選考に時間をいただいてしまいました。
提案者の皆様の非常にクオリティの高い提案に加え、さまざまな方向性のデザインがありとても良い勉強になりました。

```html
<!DOCTYPE html>
<html lang="ja">
<head>
<meta charset="utf-8">
<title>雪嶺そば 化粧箱デザイン</title>
<link href="https://fonts.googleapis.com/css2?family=Shippori+Mincho:wght@400;600;700&family=Cormorant+Garamond:wght@500&display=swap" rel="stylesheet">
<style>
  :root{
    --paper:#ffffff;
    --navy:#262d3b;
    --navy-deep:#12151d;
    --ink:#0b0c10;
    --gold:#c9a36a;
    --gold-soft:#a8895c;
    --text-soft:#b9bcc4;
    --seal:#9b2c22;
    --frame:#3b2b22;
    --frame-inner:#1a1412;
  }
  *{margin:0;padding:0;box-sizing:border-box}
  html,body{width:738px;height:1200px;overflow:hidden;background:var(--paper)}
  body{position:relative;font-family:"Shippori Mincho",serif;color:var(--text-soft)}
  .abs{position:absolute}
  .vertical{writing-mode:vertical-rl;text-orientation:upright;white-space:nowrap}

  /* lid */
  .lid{left:60px;top:25px;width:615px;height:575px;background:var(--navy)}
  .lid .rule{left:306px;top:62px;width:1px;height:18px;background:var(--text-soft)}
  .lid .tagline{left:297px;top:92px;font-size:12px;letter-spacing:4px}
  .lid .name{top:350px;font-size:40px;font-weight:600;color:var(--gold);letter-spacing:10px;line-height:1}
  .lid .name-right{left:312px}
  .lid .name-left{left:262px}
  .seal{background:var(--seal);color:#f2dcd2;font-size:9px;line-height:1;display:flex;align-items:center;justify-content:center;border-radius:1px;white-space:nowrap}
  .lid .seal{left:296px;top:448px;width:20px;height:14px}
  .lid .copy{left:0;width:615px;top:486px;text-align:center;font-size:8.5px;letter-spacing:2px}
  .info{border:1px solid var(--text-soft);color:var(--paper);text-align:center;font-size:8px;line-height:1.3}
  .info b{display:block;font-size:15px;font-weight:600}
  .lid .boil{left:242px;top:518px;width:62px;height:42px;padding-top:6px}
  .lid .weight{left:312px;top:518px;width:62px;height:42px;padding-top:14px}
  .brand-en{font-family:"Cormorant Garamond",serif;font-size:8px;line-height:1.25;letter-spacing:.5px;color:var(--text-soft);white-space:nowrap}
  .lid .brand-en{left:20px;top:530px}
  .maker-mark{border:1px solid var(--gold-soft);color:var(--gold);font-size:9px;line-height:1;display:flex;align-items:center;justify-content:center;writing-mode:vertical-rl;white-space:nowrap;letter-spacing:1px}
  .lid .maker-mark{left:565px;top:512px;width:30px;height:50px}

  /* gift box */
  .giftbox{left:60px;top:625px;width:615px;height:550px;background:var(--frame)}
  .giftbox .tray{position:absolute;inset:12px;background:var(--frame-inner)}
  .packs{position:absolute;left:30px;top:24px;right:30px;bottom:24px;display:flex;gap:8px}
  .pack{position:relative;flex:1;background:linear-gradient(180deg,var(--navy) 0%,var(--navy) 52%,var(--navy-deep) 100%);border:1px solid #3c4252}
  .pack .rule{left:50%;top:22px;width:1px;height:14px;background:var(--text-soft)}
  .pack .tagline{left:calc(50% - 4px);top:44px;font-size:7px;letter-spacing:2px;line-height:1}
  .pack .name{top:134px;font-size:22px;font-weight:600;color:var(--gold);letter-spacing:6px;line-height:1}
  .pack .name-right{left:calc(50% + 2px)}
  .pack .name-left{left:calc(50% - 26px)}
  .pack .seal{left:calc(50% - 6px);top:192px;width:14px;height:10px;font-size:6px}
  .pack .ridge{left:0;right:0;top:212px;height:56px;background:linear-gradient(180deg,rgba(230,232,238,0) 0%,rgba(214,218,226,.75) 35%,rgba(60,66,80,.6) 75%,rgba(18,21,29,0) 100%)}
  .pack .brand-en{left:10px;bottom:20px;font-size:6.5px}
  .pack .maker-mark{right:10px;bottom:14px;width:22px;height:38px;font-size:7px}
</style>
</head>
<body>

<section class="lid abs">
  <div class="rule abs"></div>
  <p class="tagline vertical abs">本場信州の伝統の味</p>
  <h1 class="name name-right vertical abs">雪嶺</h1>
  <p class="name name-left vertical abs">そば</p>
  <div class="seal abs">謹製</div>
  <p class="copy abs">そばの豊かな香りと喉ごしの良さを楽しめます</p>
  <div class="info boil abs">ゆで時間<b>4~5分</b></div>
  <div class="info weight abs">内容量220g</div>
  <p class="brand-en abs">Yukine Noodle Works<br>Sekirei Soba</p>
  <div class="maker-mark abs">山里製麺</div>
</section>

<section class="giftbox abs">
  <div class="tray"></div>
  <div class="packs">
    <article class="pack">
      <div class="rule abs"></div>
      <p class="tagline vertical abs">本場信州の伝統の味</p>
      <p class="name name-right vertical abs">雪嶺</p>
      <p class="name name-left vertical abs">そば</p>
      <div class="seal abs">謹製</div>
      <div class="ridge abs" role="img" aria-label="雪をかぶった山並みのイラスト"></div>
      <p class="brand-en abs">Yukine Noodle Works<br>Sekirei Soba</p>
      <div class="maker-mark abs">山里製麺</div>
    </article>
    <article class="pack">
      <div class="rule abs"></div>
      <p class="tagline vertical abs">本場信州の伝統の味</p>
      <p class="name name-right vertical abs">雪嶺</p>
      <p class="name name-left vertical abs">そば</p>
      <div class="seal abs">謹製</div>
      <div class="ridge abs" role="img" aria-label="雪をかぶった山並みのイラスト"></div>
      <p class="brand-en abs">Yukine Noodle Works<br>Sekirei Soba</p>
      <div class="maker-mark abs">山里製麺</div>
    </article>
    <article class="pack">
      <div class="rule abs"></div>
      <p class="tagline vertical abs">本場信州の伝統の味</p>
      <p class="name name-right vertical abs">雪嶺</p>
      <p class="name name-left vertical abs">そば</p>
      <div class="seal abs">謹製</div>
      <div class="ridge abs" role="img" aria-label="雪をかぶった山並みのイラスト"></div>
      <p class="brand-en abs">Yukine Noodle Works<br>Sekirei Soba</p>
      <div class="maker-mark abs">山里製麺</div>
    </article>
    <article class="pack">
      <div class="rule abs"></div>
      <p class="tagline vertical abs">本場信州の伝統の味</p>
      <p class="name name-right vertical abs">雪嶺</p>
      <p class="name name-left vertical abs">そば</p>
      <div class="seal abs">謹製</div>
      <div class="ridge abs" role="img" aria-label="雪をかぶった山並みのイラスト"></div>
      <p class="brand-en abs">Yukine Noodle Works<br>Sekirei Soba</p>
      <div class="maker-mark abs">山里製麺</div>
    </article>
  </div>
</section>

</body>
</html>
```